Professional business card for Real Estate Industry. Providing logo.
Name: Mirna Toveck, Senior Executive Associate
Business Name: BTK Summit Realty
Address: 2875 Willow Brook Lane, Roseville, CA 95612
Website: www.PhoneBTKHomes.com
Phone: 916.457.3102
Fax: 916.614.7290
Email: mirna@phonebtkhomes.com
Quality Real Estate Services Since 1991
Front of card slogan: The commitment you need, The results you deserve
Fair Dwelling Access Logo

Back side: Design - Attachment for example available

Slogan on back: There is no finer compliment than a referral from you.

```html
<!DOCTYPE html>
<html lang="en">
<head>
<meta charset="utf-8">
<title>BTK Summit Realty – Business Card</title>
<link href="https://fonts.googleapis.com/css2?family=Exo+2:wght@400;500;600&display=swap" rel="stylesheet">
<style>
  :root {
    --bg: #2e2f31;
    --olive: #7a8a24;
    --blue: #1f56a3;
    --navy: #1d3f73;
    --paper: #ffffff;
    --paper-shade: #eef0f2;
    --accent-red: #d2452c;
    --ink: #2d2d2d;
    --muted: #5f6368;
  }
  * { box-sizing: border-box; margin: 0; padding: 0; }
  html, body { width: 1200px; height: 863px; overflow: hidden; }
  body {
    background: var(--bg);
    font-family: "Exo 2", sans-serif;
    position: relative;
  }
  .card {
    position: absolute;
    width: 630px;
    height: 360px;
    overflow: hidden;
    box-shadow: 0 10px 30px rgba(0,0,0,.45);
  }

  /* Front */
  .card-front { left: 150px; top: 48px; background: var(--olive); }
  .card-front .panel {
    position: absolute;
    left: 62px; right: 62px; top: 0; bottom: 0;
    background: linear-gradient(135deg, var(--paper) 55%, var(--paper-shade));
    display: flex; flex-direction: column; align-items: center;
  }
  .trim-mark { position: absolute; width: 30px; height: 2px; background: var(--accent-red); }
  .card-front .trim-mark.left { left: 0; top: 248px; }
  .card-front .trim-mark.right { right: 0; top: 52px; }

  .brand { display: flex; align-items: center; gap: 10px; }
  .brand-mark { width: 14px; height: 14px; background: var(--olive); flex: none; }
  .brand-name {
    font-weight: 600;
    color: var(--navy);
    text-transform: uppercase;
    letter-spacing: .5px;
  }
  .brand-tagline { font-size: 11px; color: var(--muted); margin-top: 5px; text-align: center; }

  .card-front .brand { margin-top: 128px; }
  .card-front .brand-name { font-size: 28px; }
  .card-front .website {
    margin-top: 56px;
    font-size: 19px; font-weight: 500; color: var(--ink);
  }

  /* Back */
  .card-back { left: 420px; top: 455px; background: var(--blue); }
  .card-back .logo-square {
    position: absolute; left: 36px; top: 40px;
    width: 280px; height: 280px;
    background: linear-gradient(135deg, var(--paper) 60%, var(--paper-shade));
    display: flex; flex-direction: column; align-items: center; justify-content: center;
    padding: 0 20px;
  }
  .card-back .brand-name { font-size: 20px; }
  .card-back .brand-tagline { font-size: 10px; }
  .referral {
    margin-top: 26px;
    font-size: 11px; font-style: normal; color: var(--navy);
    text-align: center; line-height: 1.35;
  }
  .card-back .trim-mark { left: 0; top: 150px; background: var(--olive); }

  .details {
    position: absolute; left: 330px; right: 26px; top: 34px;
    color: var(--paper); text-align: right;
  }
  .person-name { font-size: 24px; font-weight: 500; letter-spacing: 1.5px; text-transform: uppercase; }
  .person-title { font-size: 13px; letter-spacing: 1px; text-transform: uppercase; margin-top: 4px; }
  .divider { height: 2px; background: var(--olive); margin: 16px 0 18px 10px; }

  .contact-row { display: flex; justify-content: flex-end; align-items: center; gap: 12px; margin-bottom: 12px; }
  .contact-row p { font-size: 14px; line-height: 1.25; letter-spacing: .3px; }
  .icon {
    width: 30px; height: 30px; border-radius: 5px;
    background: var(--olive);
    display: flex; align-items: center; justify-content: center; flex: none;
  }
  .icon svg { width: 16px; height: 16px; }
</style>
</head>
<body>

  <section class="card card-front" aria-label="Card front">
    <span class="trim-mark left"></span>
    <span class="trim-mark right"></span>
    <div class="panel">
      <div class="brand">
        <span class="brand-mark"></span>
        <span class="brand-name">BTK Summit Realty</span>
      </div>
      <p class="brand-tagline">The commitment you need, The results you deserve</p>
      <p class="website">www.PhoneBTKHomes.com</p>
    </div>
  </section>

  <section class="card card-back" aria-label="Card back">
    <span class="trim-mark"></span>
    <div class="logo-square">
      <div class="brand">
        <span class="brand-mark"></span>
        <span class="brand-name">BTK Summit Realty</span>
      </div>
      <p class="brand-tagline">Quality Real Estate Services Since 1991</p>
      <p class="referral">There is no finer compliment<br>than a referral from you.</p>
    </div>

    <div class="details">
      <h1 class="person-name">Mirna Toveck</h1>
      <p class="person-title">Senior Executive Associate</p>
      <div class="divider"></div>

      <div class="contact-row">
        <p>2875 Willow Brook Lane<br>Roseville, CA 95612</p>
        <span class="icon">
          <svg viewBox="0 0 24 24" fill="#fff"><path d="M12 2a7 7 0 0 0-7 7c0 5 7 13 7 13s7-8 7-13a7 7 0 0 0-7-7zm0 9.5A2.5 2.5 0 1 1 12 6.5a2.5 2.5 0 0 1 0 5z"/></svg>
        </span>
      </div>
      <div class="contact-row">
        <p>P 916.457.3102<br>F 916.614.7290</p>
        <span class="icon">
          <svg viewBox="0 0 24 24" fill="#fff"><path d="M6.6 10.8a15 15 0 0 0 6.6 6.6l2.2-2.2a1 1 0 0 1 1-.25 11.4 11.4 0 0 0 3.6.6 1 1 0 0 1 1 1V20a1 1 0 0 1-1 1A17 17 0 0 1 3 4a1 1 0 0 1 1-1h3.5a1 1 0 0 1 1 1c0 1.25.2 2.45.6 3.6a1 1 0 0 1-.25 1z"/></svg>
        </span>
      </div>
      <div class="contact-row">
        <p>mirna@phonebtkhomes.com<br>www.PhoneBTKHomes.com</p>
        <span class="icon">
          <svg viewBox="0 0 24 24" fill="none" stroke="#fff" stroke-width="1.8"><circle cx="12" cy="12" r="9"/><path d="M3 12h18M12 3c3 3.5 3 14.5 0 18M12 3c-3 3.5-3 14.5 0 18"/></svg>
        </span>
      </div>
    </div>
  </section>

</body>
</html>
```